Webdesign for Brightwell for use on webpage

We aim to deliver insights for power consumers in the nordic market in the B2B market, without being a supplier.

Since we are helping customers in the green transition and reducing CO2 emissions, green colors would be preferred, but we are keeping an open mind. We would like to communicate transperancy, awareness and enabling economic potential for customers.

We deliver our product on a SaaS platform through visualization in dashboards

Target Market(s)

B2B

Industry/Entity Type

Power Consumption

Number of Pages Required

1 page

Colors
0054AA
0677BA
7BADD7
CADEEF
E8F1F8
0094D4
00A9DD
6FCCEA
C7EBF8
E9F6FB
00AB8E
00BBA5
67D7C9
C6EFE9
E9F9F6
59FF00
82FF00
B8FF75
E3FFCB
F4FFEA

Requirements
Must have
• The general looks and color schemes must be in line with logo called "brightwell.eps" - see attached

```html
<!DOCTYPE html>
<html lang="en">
<head>
<meta charset="utf-8">
<title>Brightwell — Scope 3 Greenhouse Gas Reporting</title>
<link rel="stylesheet" href="https://fonts.googleapis.com/css2?family=Questrial&family=Outfit:wght@500;600&family=Ubuntu:wght@300;400;500&display=swap">
<style>
  :root {
    --lime: #6cf51c;
    --lime-bright: #59ff00;
    --ink: #111111;
    --text: #333333;
    --muted: #555555;
    --navy: #0054aa;
    --card: #5a5a5a;
    --white: #ffffff;
    --sky-1: #e9f1f8;
    --sky-2: #9fc3df;
    --sky-3: #6f9fc6;
    --ground: #4b5560;
  }
  * { box-sizing: border-box; margin: 0; padding: 0; }
  html, body { width: 848px; height: 1200px; overflow: hidden; background: var(--white); }
  body { position: relative; font-family: "Ubuntu", sans-serif; color: var(--text); }

  .top-bar { position: absolute; left: 40px; top: 52px; width: 772px; height: 34px; background: var(--lime); }
  .social { position: absolute; left: 46px; top: 10px; display: flex; gap: 4px; }
  .social span { width: 14px; height: 14px; background: var(--ink); border-radius: 2px; }
  .menu-toggle { position: absolute; right: 50px; top: 10px; width: 28px; height: 15px; }

  .hero { position: absolute; left: 40px; top: 87px; width: 772px; height: 354px;
    background: linear-gradient(90deg, #ffffff 0%, rgba(255,255,255,0.85) 22%, rgba(255,255,255,0) 50%),
                linear-gradient(180deg, var(--sky-3) 0%, var(--sky-2) 30%, var(--sky-1) 60%, #c9d3db 78%, var(--ground) 100%); }

  .nav { position: absolute; top: 87px; left: 553px; display: flex; font-family: "Questrial", sans-serif; font-size: 8.5px; }
  .nav a { display: block; height: 25px; line-height: 23px; color: #333; text-decoration: none; text-align: center; }
  .nav .home { width: 70px; background: var(--lime); }
  .nav .about { width: 73px; }
  .nav .contact { width: 72px; }

  .brand { position: absolute; left: 84px; top: 126px; display: flex; align-items: center; gap: 6px; }
  .brand-dot { width: 16px; height: 16px; border-radius: 50%; background: var(--navy); }
  .brand-name { font-family: "Ubuntu", sans-serif; font-weight: 500; font-size: 15px; color: var(--navy); line-height: 16px; }

  .hero-title { position: absolute; left: 88px; top: 192px; width: 240px; font-family: "Questrial", sans-serif; font-weight: 400; font-size: 26px; line-height: 31px; color: #222; }
  .hero-lead { position: absolute; left: 87px; top: 336px; width: 200px; font-family: "Outfit", sans-serif; font-weight: 500; font-size: 11.4px; line-height: 13.9px; color: var(--ink); }

  .contact-card { position: absolute; left: 430px; top: 345px; width: 260px; height: 377px; background: var(--card); border-radius: 24px; }
  .contact-card h2 { position: absolute; top: 71px; width: 100%; text-align: center; font-family: "Outfit", sans-serif; font-weight: 600; font-size: 21px; color: var(--white); letter-spacing: 0.4px; }
  .field { position: absolute; left: 25px; width: 214px; background: var(--white); border-radius: 3px; font-size: 5.5px; color: #9aa8b8; padding: 6px 5px; }
  .field.name { top: 134px; height: 20px; }
  .field.email { top: 172px; height: 20px; }
  .field.message { top: 211px; height: 56px; border-radius: 6px; padding-top: 4px; }
  .send { position: absolute; left: 84px; top: 291px; width: 96px; height: 20px; background: var(--lime-bright); border-radius: 2px; color: var(--white); font-family: "Ubuntu", sans-serif; font-weight: 500; font-size: 8.5px; text-align: center; line-height: 20px; }

  .feature { position: absolute; left: 86px; width: 300px; }
  .feature svg { position: absolute; left: 0; top: -6px; }
  .feature h3 { position: absolute; left: 37px; top: 0; font-weight: 500; font-size: 12.5px; color: #222; letter-spacing: 0.2px; white-space: nowrap; }
  .feature p { position: absolute; left: 37px; top: 25px; width: 226px; font-weight: 300; font-size: 9.2px; line-height: 13.7px; color: var(--muted); }
  .feature b { font-weight: 500; color: #222; }
  .f1 { top: 478px; } .f2 { top: 583px; } .f3 { top: 688px; }

  .benefit { position: absolute; top: 848px; width: 219px; }
  .benefit-photo { width: 219px; height: 123px; }
  .benefit h3 { position: absolute; top: 149px; width: 219px; font-weight: 500; font-size: 13.2px; line-height: 14px; color: #222; letter-spacing: 0.2px; }
  .benefit p { position: absolute; top: 177px; width: 210px; font-weight: 300; font-size: 11.2px; line-height: 16px; color: var(--muted); }
  .benefit b { font-weight: 500; color: #222; }
  .b1 { left: 80px; } .b2 { left: 314px; } .b3 { left: 548px; }
  .b1 p { top: 181px; }
</style>
</head>
<body>

<header class="top-bar">
  <div class="social" aria-label="Social links"><span></span><span></span><span></span></div>
  <svg class="menu-toggle" viewBox="0 0 28 15" aria-label="Menu"><rect y="0" width="28" height="3" fill="#111"/><rect y="6" width="28" height="3" fill="#111"/><rect y="12" width="28" height="3" fill="#111"/></svg>
</header>

<section class="hero" role="img" aria-label="Wind turbines on snowy hills under a blue cloudy sky"></section>

<nav class="nav">
  <a class="home" href="#">HOME</a>
  <a class="about" href="#">ABOUT</a>
  <a class="contact" href="#">CONTACT</a>
</nav>

<div class="brand">
  <span class="brand-dot"></span>
  <span class="brand-name">Brightwell</span>
</div>

<h1 class="hero-title">Automate Scope 3 Greenhouse Gas Reporting and Tracking.</h1>
<p class="hero-lead">Our Scope 3 Greenhouse Gas (GHG) solution automates supplier data collection for Scope 1, 2, and 3 and provides the business insights you need to mitigate carbon emissions and make a positive impact on climate change.</p>

<section class="contact-card">
  <h2>CONTACT US</h2>
  <div class="field name">Name</div>
  <div class="field email">Email</div>
  <div class="field message">Messages</div>
  <div class="send">Send Message</div>
</section>

<article class="feature f1">
  <svg width="24" height="24" viewBox="0 0 24 24"><rect x="5" y="3" width="14" height="19" rx="1.5" fill="none" stroke="#3fbf3a" stroke-width="1.4"/><rect x="9" y="1.5" width="6" height="3" fill="#3fbf3a"/><path d="M8 9h8M8 12.5h8M8 16h8" stroke="#3fbf3a" stroke-width="1.2"/></svg>
  <h3>Follow The GHG Protocol</h3>
  <p>Our solution <b>follows GHG Protocol guidelines for carbon emissions</b>. Our reporting template gathers information to satisfy EPA and global GHG regulation requirements.</p>
</article>

<article class="feature f2">
  <svg width="24" height="24" viewBox="0 0 24 24"><rect x="3" y="4" width="17" height="17" rx="1" fill="none" stroke="#3fbf3a" stroke-width="2"/><path d="M7 12l4 4 10-11" fill="none" stroke="#3fbf3a" stroke-width="2.4"/></svg>
  <h3>Easily Get The Data You Need</h3>
  <p>We combine <b>comprehensive supplier data collection at both the energy and GHG levels</b> with sophisticated reporting to provide exactly what you need for your GHG inventory reporting requirements.</p>
</article>

<article class="feature f3">
  <svg width="26" height="24" viewBox="0 0 26 24"><path d="M2 20l6-7 5 4 10-11" fill="none" stroke="#3fbf3a" stroke-width="2"/><circle cx="4" cy="8" r="1.3" fill="#3fbf3a"/><circle cx="17" cy="4" r="1.3" fill="#3fbf3a"/></svg>
  <h3>Dynamic Carbon Emissions Reporting</h3>
  <p><b>Easily generate comprehensive reports and visualizations</b> to see a wide variety of breakdowns. Compare year over year and track your progress.</p>
</article>

<article class="benefit b1">
  <div class="benefit-photo" role="img" aria-label="Two colleagues in discussion at an office desk" style="background:linear-gradient(135deg,#c9ccd0,#6d7480 60%,#3c4048)"></div>
  <h3>Gain Expertise And GHG Resources</h3>
  <p>Our team of regulatory experts is comprised of PhDs and scientists. <b>We ensure you and your supply chain are completely knowledgeable with Greenhouse Gas resources</b> and a 24/7, multilingual supplier help center.</p>
</article>

<article class="benefit b2">
  <div class="benefit-photo" role="img" aria-label="Office team celebrating and throwing papers in the air" style="background:linear-gradient(135deg,#d8d6d2,#9a9692 55%,#5e5a58)"></div>
  <h3>Eliminate Manual Work</h3>
  <p>Collecting compliance data and documents for tracking your supply chain carbon footprint can be difficult and time-consuming on your own. <b>We automate the entire process and take it off your plate</b>.</p>
</article>

<article class="benefit b3">
  <div class="benefit-photo" role="img" aria-label="Business people at a laptop with overlaid data charts" style="background:linear-gradient(135deg,#e4e2e4,#a89a9c 50%,#5a4e52)"></div>
  <h3>Customizable GHG Software</h3>
  <p>Every business is unique in the compliance challenges it faces, so why settle for a one-size-fits-all solution? <b>We offer custom Scope 3 Carbon Emissions software solutions to best suit your needs</b>.</p>
</article>

</body>
</html>
```